Financial Planning business needs a new Business Card design

We need a business card design for an Australian financial planning business. I am looking for a clean simple design

Target Market(s)

People aged 25-40

Industry/Entity Type

Financial Service

Contact Information for Business Card

On the front of the card we need the following information:
Name: Colin Merrow (First Name Green: #006838 and last name Grey: #414042)
Position: Financial Adviser
Qualifications: BEc(Hons), AdDipFS(FP), Dip FMBM, CFL®
Mobile: 0437 512 604
Email: colin@brightledgeplan.com.au

On the back of the card we need:
Postal address: PO BOX 5307, PERTH BC, WA 6849
Website: www.brightledgeplan.com.au
Text: AFS Licence No. 518760

The fields need to be able to be edited.

Font styles to use
Sans Serif

Requirements
Must have
• Information listed above

```html
<!DOCTYPE html>
<html lang="en">
<head>
<meta charset="utf-8">
<title>Brightledge Plan – Business Card</title>
<link href="https://fonts.googleapis.com/css2?family=Montserrat:wght@400;500;700;800&display=swap" rel="stylesheet">
<style>
  :root {
    --canvas: #e4e4e2;
    --card-dark: #464646;
    --card-white: #ffffff;
    --brand-green: #006838;
    --text-grey: #414042;
    --divider: #3a3a3a;
  }
  * { margin: 0; padding: 0; box-sizing: border-box; }
  html, body {
    width: 1200px; height: 900px; overflow: hidden;
    background: var(--canvas);
    font-family: "Montserrat", sans-serif;
  }
  .canvas {
    position: relative; width: 1200px; height: 900px;
  }
  .card {
    position: absolute; left: 320px;
    width: 560px; height: 320px;
    border-radius: 22px; overflow: hidden;
    box-shadow: 0 10px 30px rgba(0,0,0,.18);
  }
  /* back */
  .card-back { top: 80px; background: var(--card-dark); }
  .card-back .wordmark {
    position: absolute; left: 0; right: 0; top: 118px;
    text-align: center; color: #fff;
    font-weight: 800; font-size: 44px; letter-spacing: 1px;
    text-transform: uppercase; line-height: 1;
  }
  .card-back .website {
    position: absolute; left: 0; right: 0; bottom: 38px;
    text-align: center; color: #fff; font-size: 15px; font-weight: 400;
  }
  .website strong { font-weight: 700; }

  /* front */
  .card-front { top: 500px; background: var(--card-white); }
  .card-front .panel-shape { position: absolute; inset: 0; }
  .card-front .wordmark {
    position: absolute; left: 0; width: 275px; top: 148px;
    text-align: center; color: #fff;
    font-weight: 800; font-size: 25px; letter-spacing: .5px;
    text-transform: uppercase; line-height: 1.1;
  }
  .details {
    position: absolute; left: 318px; top: 40px;
    color: var(--text-grey); font-size: 12.5px; line-height: 1.3;
  }
  .name {
    font-size: 22px; font-weight: 800; letter-spacing: .5px;
    text-transform: uppercase; margin-bottom: 6px; line-height: 1;
  }
  .name .first { color: var(--brand-green); }
  .name .last { color: var(--text-grey); }
  .block { margin-bottom: 8px; }
  .licence-no { color: var(--brand-green); }
  .contact { list-style: none; }
  .contact li { display: flex; align-items: center; gap: 7px; }
  .contact svg { width: 10px; height: 10px; flex: none; }
  .contact strong { color: var(--brand-green); font-weight: 700; }
</style>
</head>
<body>
<div class="canvas">

  <section class="card card-back" aria-label="Card back">
    <div class="wordmark">Brightledge Plan</div>
    <p class="website">www.<strong>brightledgeplan</strong>.com.au</p>
  </section>

  <section class="card card-front" aria-label="Card front">
    <svg class="panel-shape" viewBox="0 0 560 320" width="560" height="320" aria-hidden="true">
      <path d="M0 0 H295 V78 L283 88 L295 98 V320 H0 Z" fill="var(--card-dark)"/>
      <path d="M300 0 V76 L288 88 L300 100 V320" fill="none" stroke="var(--divider)" stroke-width="2"/>
    </svg>
    <div class="wordmark">Brightledge<br>Plan</div>

    <div class="details">
      <h1 class="name"><span class="first">Colin</span> <span class="last">Merrow</span></h1>
      <div class="block">
        Financial Adviser<br>
        BEc(Hons), AdDipFS(FP)<br>
        Dip FMBM, CFL®
      </div>
      <div class="block">AFS Licence No. <span class="licence-no">518760</span></div>
      <div class="block">
        PO BOX 5307<br>
        PERTH BC, WA 6849
      </div>
      <ul class="contact">
        <li>
          <svg viewBox="0 0 10 10"><rect x="2.5" y="0.5" width="5" height="9" rx="1" fill="none" stroke="var(--brand-green)" stroke-width="1.2"/><circle cx="5" cy="7.8" r=".6" fill="var(--brand-green)"/></svg>
          0437 512 604
        </li>
        <li>
          <svg viewBox="0 0 10 10"><rect x=".6" y="2" width="8.8" height="6" fill="none" stroke="var(--brand-green)" stroke-width="1.1"/><path d="M.6 2 L5 5.6 L9.4 2" fill="none" stroke="var(--brand-green)" stroke-width="1.1"/></svg>
          colin@brightledgeplan.com.au
        </li>
        <li>
          <svg viewBox="0 0 10 10"><circle cx="5" cy="5" r="4.3" fill="none" stroke="var(--brand-green)" stroke-width="1.1"/><ellipse cx="5" cy="5" rx="1.8" ry="4.3" fill="none" stroke="var(--brand-green)" stroke-width=".9"/><path d="M.8 5 H9.2" stroke="var(--brand-green)" stroke-width=".9"/></svg>
          www.<strong>brightledgeplan</strong>.com.au
        </li>
      </ul>
    </div>
  </section>

</div>
</body>
</html>
```